Stationery set for Financial Consultancy based in London
Harbour Ledger
Stationery set for Financial Consultancy based in London - Financial Services
Creative Brief
Simple
Damian Ashcroft
Managing Partner
41 Pelham Row London SE7 2QD
dashcroft@harbourledger.co.uk
www.harbourledger.co.uk
Logo, should be classic, sophisticated without any coloured borders. Font colour should be black. Please please include icon from the logo. I want the business card layout to be clean and uncluttered.
Please place logo and website url on back of business card only

```html
<!DOCTYPE html>
<html lang="en">
<head>
<meta charset="utf-8">
<title>Harbour Ledger – Stationery Concepts</title>
<link href="https://fonts.googleapis.com/css2?family=Oswald:wght@500&family=Open+Sans:wght@400;600&display=swap" rel="stylesheet">
<style>
:root{
  --bg:#a9a9ab;
  --teal:#3c6478;
  --navy:#1f3b6b;
  --ink:#1d2b36;
  --paper:#ffffff;
  --rule:#d5dbe0;
  --muted:#7a8a96;
  --photo:#5a5a5a;
}
*{margin:0;padding:0;box-sizing:border-box}
html,body{width:1200px;height:254px;overflow:hidden;background:var(--bg)}
.canvas{position:relative;width:1200px;height:254px;font-family:"Open Sans",sans-serif;color:var(--ink)}
.piece{position:absolute;background:var(--paper);overflow:hidden}
.slide{position:absolute;width:93px;height:70px;background:var(--paper);overflow:hidden}
.teal,.slide.teal,.piece.teal{background:var(--teal);color:#fff}
.navy,.piece.navy{background:var(--navy);color:#fff}
.brand{font-family:"Oswald",sans-serif;font-weight:500;color:var(--ink);letter-spacing:.04em;text-transform:uppercase;display:flex;align-items:center;gap:2px;line-height:1;white-space:nowrap}
.brand .mark{display:inline-block;background:currentColor}
.on-dark .brand,.brand.light{color:#fff}
.center{display:flex;justify-content:center}
.tiny{font-size:2.2px;line-height:1.4;color:var(--muted);white-space:nowrap}
.on-dark .tiny{color:#dfe7ec}
.footer{position:absolute;left:0;right:0;bottom:3px;text-align:center}
.contact{position:absolute;right:5px;top:6px;text-align:left}
.title-block{position:absolute;left:10px;top:30px;width:40px;text-align:center}
.title-block .sub{font-size:3.6px;color:var(--teal);margin-top:2px;white-space:nowrap}
.fax-table{position:absolute;left:4px;right:4px;top:26px;display:grid;grid-template-columns:10% 40% 10% 40%;gap:1px;font-size:2px}
.fax-table span{height:3.5px;border-bottom:.3px solid var(--rule);color:var(--ink)}
.fax-table span.f{background:#eef1f3}
.disc{position:absolute;border-radius:50%;display:flex;flex-direction:column;align-items:center;justify-content:flex-start}
.disc .hole{position:absolute;left:50%;top:50%;width:36%;height:36%;transform:translate(-50%,-50%);border-radius:50%;background:#fff;border:3px solid #1a1a1a}
.disc .brand{margin-top:10%}
.slide h3{position:absolute;left:5px;top:4px;font-size:3.6px;font-weight:600;color:var(--teal)}
.slide h4{position:absolute;left:5px;top:8.5px;font-size:2.2px;font-weight:600;color:var(--teal)}
.slide .hr{position:absolute;left:5px;right:5px;top:11.5px;height:.4px;background:var(--rule)}
.slide .corner{position:absolute;right:5px;top:4px;width:3.5px;height:4.5px;background:var(--teal)}
.photos{position:absolute;left:5px;right:5px;top:15px;display:grid;grid-template-columns:repeat(4,1fr);gap:3px}
.photos .ph{height:16px;background:var(--photo);font-size:2px;color:#ccc;display:flex;align-items:center;justify-content:center}
.photos .cap{font-size:1.9px;color:var(--teal);line-height:1.4;margin-top:1px}
.body{font-size:1.8px;line-height:1.5;color:var(--muted)}
.label{font-size:2px;color:var(--teal);font-weight:600}
.thanks-title{position:absolute;left:0;right:0;top:22px;text-align:center;font-size:11px;line-height:1;color:#fff}
.thanks-sub{position:absolute;left:0;right:0;top:36px;text-align:center;font-size:6px;line-height:1;color:#fff}
</style>
</head>
<body>
<div class="canvas">

  <div class="title-block">
    <div class="brand center" style="font-size:4.4px"><span class="mark" style="width:4px;height:4px"></span>Harbour Ledger</div>
    <div class="sub">Stationery Concepts</div>
  </div>

  <div class="piece" style="left:6px;top:57px;width:47px;height:26px">
    <div class="brand" style="position:absolute;left:3px;top:4px;font-size:2.8px">Harbour Ledger</div>
    <div class="tiny" style="position:absolute;left:3px;top:11px">
      41 Pelham Row London SE7 2QD<br>+44 (0)20 7946 0182<br>dashcroft@harbourledger.co.uk<br>www.harbourledger.co.uk
    </div>
    <div style="position:absolute;right:3px;top:12px;text-align:right;font-size:2.2px;line-height:1.3">
      <div style="color:var(--teal);font-weight:600">Damian Ashcroft</div><div class="tiny">Managing Partner</div>
    </div>
    <div style="position:absolute;right:0;top:15px;width:1.2px;height:5px;background:var(--navy)"></div>
  </div>

  <div class="piece teal on-dark" style="left:6px;top:90px;width:47px;height:27px">
    <div class="brand center" style="position:absolute;left:0;right:0;top:10px;font-size:2.8px">Harbour Ledger</div>
    <div class="tiny footer">www.harbourledger.co.uk</div>
  </div>

  <div class="piece" style="left:56px;top:15px;width:79px;height:102px">
    <div class="brand" style="position:absolute;left:6px;top:7px;font-size:2.8px">Harbour Ledger</div>
    <div class="tiny contact">41 Pelham Row<br>London SE7 2QD<br>+44 (0)20 7946 0182<br>www.harbourledger.co.uk</div>
    <div class="tiny footer">www.harbourledger.co.uk</div>
  </div>
  <div class="piece" style="left:140px;top:15px;width:79px;height:102px">
    <div class="brand center" style="position:absolute;left:0;right:0;top:7px;font-size:2.8px">Harbour Ledger</div>
    <div class="tiny footer">41 Pelham Row London SE7 2QD · +44 (0)20 7946 0182 · dashcroft@harbourledger.co.uk</div>
  </div>

  <div class="piece" style="left:240px;top:42px;width:53px;height:26px">
    <div class="brand" style="position:absolute;left:3px;top:4px;font-size:2.6px">Harbour Ledger</div>
    <div class="tiny" style="position:absolute;left:3px;top:11px">+44 (0)20 7946 0182<br>dashcroft@harbourledger.co.uk<br>www.harbourledger.co.uk</div>
    <div style="position:absolute;right:3px;top:11px;text-align:right;font-size:2px;line-height:1.3"><div style="color:var(--teal);font-weight:600">Damian Ashcroft</div><div class="tiny">Managing Partner</div></div>
  </div>

  <div class="piece" style="left:223px;top:80px;width:85px;height:37px">
    <div class="brand" style="position:absolute;left:4px;top:4px;font-size:2.6px">Harbour Ledger</div>
    <div class="tiny" style="position:absolute;left:4px;top:9px">41 Pelham Row London SE7 2QD</div>
  </div>
  <div class="piece navy on-dark" style="left:322px;top:40px;width:85px;height:14px">
    <div class="brand center" style="position:absolute;left:0;right:0;top:5px;font-size:2.4px">Harbour Ledger</div>
  </div>
  <div class="piece teal on-dark" style="left:318px;top:60px;width:85px;height:14px">
    <div class="brand center" style="position:absolute;left:0;right:0;top:5px;font-size:2.4px">Harbour Ledger</div>
  </div>
  <div class="piece" style="left:311px;top:80px;width:85px;height:37px">
    <div class="brand center" style="position:absolute;left:0;right:0;top:4px;font-size:2.4px">Harbour Ledger</div>
    <div class="tiny footer">www.harbourledger.co.uk</div>
  </div>

  <div class="piece teal on-dark" style="left:412px;top:18px;width:63px;height:100px">
    <div class="tiny" style="position:absolute;left:8px;top:60px">41 Pelham Row London SE7 2QD<br>+44 (0)20 7946 0182<br>www.harbourledger.co.uk</div>
  </div>
  <div class="piece" style="left:475px;top:18px;width:62px;height:72px">
    <div class="brand center" style="position:absolute;left:0;right:0;top:30px;font-size:3.8px;color:var(--navy)">Harbour Ledger</div>
  </div>
  <div class="piece teal" style="left:475px;top:90px;width:62px;height:28px"></div>

  <div class="piece" style="left:542px;top:15px;width:78px;height:102px">
    <div class="brand" style="position:absolute;left:4px;top:6px;font-size:2.6px">Harbour Ledger</div>
    <div class="tiny contact">+44 (0)20 7946 0182<br>www.harbourledger.co.uk</div>
    <div class="fax-table"><span>To</span><span class="f"></span><span>From</span><span class="f"></span><span>Fax</span><span class="f"></span><span>Pages</span><span class="f"></span><span>Phone</span><span class="f"></span><span>Date</span><span class="f"></span><span>Re</span><span class="f"></span><span>CC</span><span class="f"></span></div>
    <div style="position:absolute;left:4px;top:53px;font-size:2px">Comments :</div>
    <div class="tiny footer">41 Pelham Row London SE7 2QD</div>
  </div>
  <div class="piece" style="left:625px;top:15px;width:78px;height:102px">
    <div class="brand center" style="position:absolute;left:0;right:0;top:6px;font-size:2.6px">Harbour Ledger</div>
    <div class="fax-table"><span>To</span><span class="f"></span><span>From</span><span class="f"></span><span>Fax</span><span class="f"></span><span>Pages</span><span class="f"></span><span>Phone</span><span class="f"></span><span>Date</span><span class="f"></span><span>Re</span><span class="f"></span><span>CC</span><span class="f"></span></div>
    <div style="position:absolute;left:4px;top:53px;font-size:2px">Comments :</div>
    <div class="tiny footer">41 Pelham Row London SE7 2QD</div>
  </div>

  <div class="piece" style="left:717px;top:27px;width:86px;height:38px">
    <div class="brand" style="position:absolute;left:5px;top:7px;font-size:2.6px">Harbour Ledger</div>
    <div class="tiny contact">+44 (0)20 7946 0182<br>www.harbourledger.co.uk</div>
    <div style="position:absolute;left:0;right:0;top:23px;text-align:center;font-size:4.6px;color:var(--teal)">With Compliments</div>
  </div>

  <div class="piece" style="left:711px;top:73px;width:48px;height:36px">
    <div class="brand center" style="position:absolute;left:0;right:0;top:6px;font-size:2.4px">Harbour Ledger</div>
    <div style="position:absolute;left:0;right:0;top:21px;text-align:center;font-size:5.8px;color:var(--teal)">Thank you</div>
  </div>
  <div class="piece teal on-dark" style="left:766px;top:73px;width:47px;height:36px">
    <div class="tiny footer">www.harbourledger.co.uk</div>
  </div>

  <div class="disc teal on-dark" style="left:818px;top:7px;width:58px;height:58px">
    <div class="brand" style="font-size:2.4px">Harbour Ledger</div><div class="hole"></div>
  </div>
  <div class="piece" style="left:882px;top:10px;width:56px;height:50px">
    <div class="brand" style="position:absolute;left:4px;top:12px;font-size:2.4px">Harbour Ledger</div>
    <div class="tiny footer">41 Pelham Row London SE7 2QD</div>
  </div>

  <div class="disc teal on-dark" style="left:690px;top:128px;width:58px;height:58px"><div class="brand" style="font-size:2.4px">Harbour Ledger</div><div class="hole" style="border-color:#fff"></div></div>
  <div class="disc" style="left:757px;top:128px;width:58px;height:58px;background:#111"><div class="brand light" style="font-size:2.4px">Harbour Ledger</div><div class="hole" style="border-color:#444"></div></div>
  <div class="disc" style="left:692px;top:190px;width:58px;height:58px;background:#fff;border:2px solid var(--teal)"><div class="brand" style="font-size:2.4px">Harbour Ledger</div><div class="hole"></div></div>
  <div class="disc navy on-dark" style="left:759px;top:190px;width:58px;height:58px"><div class="brand" style="font-size:2.4px">Harbour Ledger</div><div class="hole" style="border-color:#fff"></div></div>

  <div class="piece teal on-dark" style="left:832px;top:143px;width:56px;height:40px">
    <div class="brand" style="position:absolute;left:4px;top:8px;font-size:2.4px">Harbour Ledger</div>
    <div class="tiny footer">41 Pelham Row London SE7 2QD</div>
  </div>
  <div class="piece" style="left:832px;top:195px;width:56px;height:40px">
    <div class="brand" style="position:absolute;left:4px;top:8px;font-size:2.4px">Harbour Ledger</div>
    <div class="tiny footer">41 Pelham Row London SE7 2QD</div>
  </div>

  <div class="piece" style="left:478px;top:138px;width:125px;height:76px">
    <div class="teal" style="position:absolute;left:4px;right:4px;bottom:0;height:30px"></div>
  </div>

  <div class="slide" style="left:975px;top:15px">
    <div class="brand center" style="position:absolute;left:0;right:0;top:24px;font-size:4.4px">Harbour Ledger</div>
    <div style="position:absolute;left:0;right:0;top:42px;text-align:center;font-size:3.6px;font-weight:600;color:var(--navy);line-height:1.3">Welcome to Our<br>Presentation Name<br><span style="font-weight:400;font-size:3px">Description</span></div>
  </div>
  <div class="slide" style="left:1075px;top:15px">
    <h3>Heading Here</h3><h4>Sub Heading</h4><div class="hr"></div><div class="corner"></div>
    <div class="photos">
      <div><div class="ph" role="img" aria-label="Team member portrait">Photo</div><div class="cap">Team member1<br>Title</div></div>
      <div><div class="ph" role="img" aria-label="Team member portrait">Photo</div><div class="cap">Team member2<br>Title</div></div>
      <div><div class="ph" role="img" aria-label="Team member portrait">Photo</div><div class="cap">Team member3<br>Title</div></div>
      <div><div class="ph" role="img" aria-label="Team member portrait">Photo</div><div class="cap">Team member4<br>Title</div></div>
    </div>
  </div>
  <div class="slide" style="left:975px;top:91px">
    <h3>Heading Here</h3><h4>Sub Heading</h4><div class="hr"></div><div class="corner"></div>
    <div style="position:absolute;left:5px;right:5px;top:16px;display:grid;grid-template-columns:1fr 1fr;gap:4px 6px">
      <div><div class="label">Group1</div><div class="body">Quarterly notes on markets and client holdings.</div></div>
      <div><div class="label">Group4</div><div class="body">Quarterly notes on markets and client holdings.</div></div>
      <div><div class="label">Group2</div><div class="body">Key figures summarised for the board.</div></div>
      <div><div class="label">Group5</div><div class="body">Key figures summarised for the board.</div></div>
    </div>
  </div>
  <div class="slide" style="left:1075px;top:91px">
    <h3>Heading Here</h3><h4>Sub Heading</h4><div class="hr"></div><div class="corner"></div>
    <svg style="position:absolute;left:8px;top:17px" width="42" height="40" viewBox="0 0 42 40">
      <line x1="0" y1="40" x2="42" y2="40" stroke="#3c6478" stroke-width=".5"/>
      <rect x="2" y="8" width="5" height="32" fill="#3c6478"/><rect x="9" y="2" width="5" height="38" fill="#3c6478"/>
      <rect x="16" y="14" width="5" height="26" fill="#3c6478"/><rect x="23" y="10" width="5" height="30" fill="#3c6478"/>
      <rect x="30" y="20" width="5" height="20" fill="#3c6478"/><rect x="37" y="26" width="4" height="14" fill="#3c6478"/>
    </svg>
    <div class="body" style="position:absolute;left:56px;top:18px;width:32px;white-space:normal">Revenue growth across six reporting periods this year.</div>
  </div>
  <div class="slide" style="left:975px;top:168px">
    <h3>Heading Here</h3><h4>Sub Heading</h4><div class="hr"></div><div class="corner"></div>
    <div class="body" style="position:absolute;left:5px;top:16px;width:38px">Allocation of assets by sector for the current fiscal quarter.</div>
    <svg style="position:absolute;left:60px;top:16px" width="24" height="24" viewBox="-12 -12 24 24">
      <circle r="11" fill="#3c6478"/>
      <path d="M0 0 L0 -11 A11 11 0 0 1 11 0 Z" fill="#1f3b6b"/>
      <path d="M0 0 L-7.8 7.8 A11 11 0 0 1 -11 0 Z" fill="#9fb3bf"/>
    </svg>
  </div>
  <div class="slide teal on-dark" style="left:1075px;top:168px">
    <div class="thanks-title">Thanks</div>
    <div class="thanks-sub">For Coming</div>
    <div class="tiny footer">41 Pelham Row London SE7 2QD · www.harbourledger.co.uk</div>
  </div>

</div>
</body>
</html>
```